Marktplatz Flohmarkt Kleinanzeigen Marktplatz
Zielgruppe
Wir sind ein Marktplatz rund um Hochzeit. D.h. bei uns können kostenlos alle Sachen (Brautkleid, Brautschuhe, Braut Accessories, Hochzeits Dekoration) zum verkauf eingestellt werden. Wie tauscho inserate, nur eben spezialisiert auf Hochzeit
Aufgabenstellung
Wir benötigen für unseren PHP Marktplatz ein Design, welches sehr Modern und ansprechend ist. Wir möchten kein Klassisches Hochzeitsportal mit den Üblichen Rosa, Beigen Farben sein, sondern möchten vor allem die Junge Zielgruppe ansprechen.
Das Design soll ein Mix aus tauscho-inserate und Stoffwandel sein, wobei uns wichtiger wäre das man sich bewusst am design von Stoffwandel orientiert.
Was uns besonders an Stoffwandel gefällt ist im Header die farbliche Leiste wo Logo und Kategorien integriert sind. Schicht und einfach, ohne schnickschnack.
ebenso wie bei Stoffwandel wird bei uns auf der Startseite folgendes integriert:
-Werbung (Banner)
-Plaudernetz
-Forum
Aktuelle menüs auf der Startseite:
-Home
-Marktplatz
-Gesuche (wobei gesuche kann im Layout integriert werden)
-Dienstleister (Händler und Dienstleister)
-Gruppen (das kann en einer anderen Stelle integriert werden)
-Forum (noch nicht integriert, aber beachten beim Layout, da es eingebaut wird)
-Veranstaltungen / Events
-Über Uns
(alles was aktuell im Screenshot zu sehen ist, wird aus der Leiste entfernt und im Footer eingebaut)
Anhang:
-Logo
-Screenshot unseres Aktuellen marktplatzes (noch nicht Online)
-Screenshot von StoffWandel
Design:
-Startseite
-Artikelseite (wenn der Private Kunde eine anzeige einstellt)
-Ansprechende Anmeldeseite inkl. Darstellung unserer Pakete für Privat / Händler / Dienstleister

```html
<!DOCTYPE html>
<html lang="de">
<head>
<meta charset="utf-8">
<title>Hochzeitsbasar – Marktplatz</title>
<link href="https://fonts.googleapis.com/css2?family=Arimo:wght@400;700&display=swap" rel="stylesheet">
<style>
:root{
  --pink:#e4097f;
  --pink-dark:#b5005f;
  --bg:#eeeeee;
  --white:#ffffff;
  --grey:#c8c8c8;
  --text:#555555;
  --line:#e6e6e6;
  --icon:#9a9a9a;
}
*{box-sizing:border-box;margin:0;padding:0}
html,body{width:696px;height:1200px;overflow:hidden}
body{background:var(--bg);font-family:"Arimo",Arial,sans-serif;color:var(--text);position:relative;font-size:7px}
.topbar{position:absolute;top:0;left:0;width:696px;height:15px;background:var(--white);text-align:right;padding:4px 72px 0 0;font-size:6px;color:var(--pink)}
.topbar span{margin:0 3px}
.mainbar{position:absolute;top:15px;left:0;width:696px;height:42px;background:var(--pink)}
.brand{position:absolute;left:66px;top:16px;color:var(--white);font-weight:700;font-size:8px;line-height:10px;display:flex;align-items:center;gap:3px;white-space:nowrap}
.brand i{width:6px;height:6px;border-radius:50%;background:var(--white);display:inline-block}
.nav{position:absolute;left:148px;top:16px;display:flex;gap:19px;color:var(--white);font-size:7.6px;white-space:nowrap}
.search{position:absolute;left:522px;top:11px;width:26px;height:19px;border-radius:10px;background:var(--white)}
.login{position:absolute;left:553px;top:11px;width:71px;height:19px;border-radius:10px;background:var(--white);color:var(--pink);font-size:7.5px;text-align:center;line-height:19px}
.sortbar{position:absolute;left:67px;top:75px;width:424px;height:31px;background:var(--white);display:flex;align-items:center;padding:0 14px}
.sortbar h1{font-weight:400;font-size:10px;color:#888;flex:1}
.sortbar .lbl{font-size:6.2px;color:#999;margin-right:6px}
.pill{background:var(--pink);color:var(--white);font-size:6.2px;padding:3px 4px;border-radius:7px}
.sortbar .alt{font-size:6.2px;color:#999;margin-left:8px}
.col{position:absolute;top:114px;width:135px;display:flex;flex-direction:column;gap:8.5px}
.c1{left:67px}.c2{left:212px}.c3{left:356px}
.card{background:var(--white)}
.photo{position:relative;background:linear-gradient(180deg,#d9d9d6,#f4f4f2 55%,#e0e0dc)}
.photo.green{background:linear-gradient(180deg,#3f5a2c,#e9ece4 45%,#f2f2ef 80%,#8a7c5c)}
.photo.warm{background:linear-gradient(180deg,#b48a55,#efe9e0 50%,#f5f3ef)}
.price{position:absolute;left:0;bottom:0;width:47px;height:21px;background:var(--pink);color:var(--white);font-size:8.5px;line-height:21px;text-align:center}
.cat{position:absolute;right:0;bottom:0;width:49px;height:13px;background:var(--grey);color:var(--white);font-size:6px;line-height:13px;text-align:center}
.info{height:44px;padding:8px 9px 0}
.info h2{font-size:7.2px;font-weight:700;color:var(--pink);line-height:9.5px;letter-spacing:.2px}
.meta{display:flex;justify-content:space-between;font-size:6.2px;margin-top:4px}
.actions{height:27px;border-top:1px solid var(--line);display:flex}
.actions div{flex:1;display:flex;align-items:center;justify-content:center}
.actions div+div{border-left:1px solid var(--line)}
.more{position:absolute;left:239px;top:1159px;width:81px;height:18px;border-radius:9px;background:var(--white);color:var(--pink);font-weight:700;font-size:6.5px;text-align:center;line-height:18px}
.box{position:absolute;left:505px;width:119px;background:var(--white)}
.box h3{background:var(--pink);color:var(--white);font-weight:400;font-size:9.5px;height:31px;line-height:31px;padding-left:14px}
.list{padding:0 5px}
.list li{list-style:none;height:20px;line-height:20px;border-bottom:1px solid var(--line);font-size:6.2px;padding:0 7px;display:flex;justify-content:space-between;align-items:center}
.list li.foot{background:#ececec;color:var(--pink);border:none}
.caret{width:0;height:0;border:2px solid transparent;border-top-color:#ccc;margin-top:2px}
.badge{background:var(--pink);color:var(--white);font-size:5px;border-radius:5px;padding:1px 4px;line-height:7px}
.promo{top:283px;height:111px;background:var(--pink);color:var(--white);text-align:center}
.promo h3{height:auto;line-height:normal;padding:10px 0 0;font-size:10px}
.promo p{font-size:6.2px;line-height:11px;padding:10px 10px 0}
.promo .reg{margin:8px auto 0;width:81px;height:18px;border-radius:9px;background:var(--pink-dark);font-size:6.2px;line-height:18px;font-weight:700;color:#e24a9c}
.banner{top:402px;height:87px;border:1px solid var(--pink);color:var(--pink);text-align:center;font-size:7.5px;padding-top:32px;line-height:9.5px}
.like{top:706px;height:199px}
.likehead{display:flex;align-items:center;gap:5px;padding:6px 9px}
.likehead .av{width:25px;height:25px;background:#ddd}
.likebtn{background:#6d84b4;color:var(--white);font-size:5.5px;padding:2px 4px;font-weight:700}
.likecount{font-size:5.2px;color:#6d84b4;padding:2px 9px;border-top:1px solid var(--line);margin:0 5px}
.faces{margin:4px 9px;width:87px;height:87px;background:linear-gradient(135deg,#8a8a80,#c9bfae 50%,#6a6a60)}
.plug{font-size:4.5px;padding:4px 9px;border-top:1px solid var(--line);margin:0 5px;display:flex;gap:3px;align-items:center}
.plug i{width:5px;height:5px;background:#3b5998;display:inline-block}
.share{top:914px;height:146px}
.share p{font-size:6.2px;line-height:11px;padding:8px 11px 4px}
.field{margin:0 5px 4px;height:19px;border:1px solid var(--line);border-radius:10px;display:flex;justify-content:space-between;align-items:center;padding-left:6px;font-size:6.2px;color:#999}
.field i{width:25px;height:19px;border-radius:10px;background:var(--pink);display:block;margin-right:-1px}
.news{top:1069px;height:66px}
.news .field{margin-top:9px}
.footer{position:absolute;left:512px;top:1144px;width:112px;font-size:5.8px;color:#666;line-height:7.5px}
.footer .links{margin-top:6px;font-size:5.3px}
</style>
</head>
<body>
<div class="topbar"><span>Hilfe</span>|<span>Mein Konto</span>|<span>Warenkorb (0)</span></div>
<header class="mainbar">
  <div class="brand"><i></i>Hochzeitsbasar</div>
  <nav class="nav"><span>Marktplatz</span><span>Dienstleister</span><span>Gruppen</span><span>Forum</span><span>Veranstaltungen</span><span>Über uns</span></nav>
  <div class="search"><svg width="26" height="19" viewBox="0 0 26 19"><circle cx="12.5" cy="9" r="2.6" fill="none" stroke="#aaa" stroke-width="1.1"/><line x1="14.4" y1="10.9" x2="16" y2="12.5" stroke="#aaa" stroke-width="1.1"/></svg></div>
  <div class="login">Einloggen</div>
</header>

<div class="sortbar"><h1>Marktplatz</h1><span class="lbl">Sortieren nach:</span><span class="pill">Datum</span><span class="alt">Preis</span></div>

<svg width="0" height="0" style="position:absolute">
  <symbol id="cart" viewBox="0 0 12 10"><path d="M1 1h2l1.3 5h5.4L11 2.5H3.6" fill="none" stroke="#9a9a9a" stroke-width="1"/><circle cx="5" cy="8.3" r=".9" fill="#9a9a9a"/><circle cx="9" cy="8.3" r=".9" fill="#9a9a9a"/></symbol>
  <symbol id="zoom" viewBox="0 0 10 10"><circle cx="4.3" cy="4.3" r="2.8" fill="none" stroke="#9a9a9a" stroke-width="1.1"/><line x1="6.3" y1="6.3" x2="8.5" y2="8.5" stroke="#9a9a9a" stroke-width="1.2"/></symbol>
</svg>

<div class="col c1">
  <article class="card"><div class="photo" style="height:163px" role="img" aria-label="Foto: kurzes weißes Brautkleid"><span class="price">69,00 €</span><span class="cat">Brautmode</span></div><div class="info"><h2>Traumhaftes Hochzeitskleid in weiß</h2><div class="meta"><span>22.08.2014</span><span>Köln/ Altstadt</span></div></div><div class="actions"><div><svg width="11" height="9"><use href="#cart"/></svg></div><div><svg width="8" height="8"><use href="#zoom"/></svg></div></div></article>
  <article class="card"><div class="photo warm" style="height:204px" role="img" aria-label="Foto: langes Brautkleid mit Stickerei"><span class="price">69,00 €</span><span class="cat">Brautmode</span></div><div class="info"><h2>Traumhaftes Hochzeitskleid in weiß</h2><div class="meta"><span>22.08.2014</span><span>Köln/ Altstadt</span></div></div><div class="actions"><div><svg width="11" height="9"><use href="#cart"/></svg></div><div><svg width="8" height="8"><use href="#zoom"/></svg></div></div></article>
  <article class="card"><div class="photo" style="height:141px" role="img" aria-label="Foto: Brautkleid mit Schleppe von hinten"><span class="price">69,00 €</span><span class="cat">Brautmode</span></div><div class="info"><h2>Traumhaftes Hochzeitskleid in weiß</h2><div class="meta"><span>22.08.2014</span><span>Köln/ Altstadt</span></div></div><div class="actions"><div><svg width="11" height="9"><use href="#cart"/></svg></div><div><svg width="8" height="8"><use href="#zoom"/></svg></div></div></article>
  <article class="card"><div class="photo" style="height:141px" role="img" aria-label="Foto: Brautkleid mit Schleppe von hinten"><span class="price">69,00 €</span><span class="cat">Brautmode</span></div><div class="info"><h2>Traumhaftes Hochzeitskleid in weiß</h2><div class="meta"><span>22.08.2014</span><span>Köln/ Altstadt</span></div></div><div class="actions"><div><svg width="11" height="9"><use href="#cart"/></svg></div><div><svg width="8" height="8"><use href="#zoom"/></svg></div></div></article>
</div>

<div class="col c2">
  <article class="card"><div class="photo" style="height:141px" role="img" aria-label="Foto: Brautkleid mit Schleppe von hinten"><span class="price">69,00 €</span><span class="cat">Brautmode</span></div><div class="info"><h2>Traumhaftes Hochzeitskleid in weiß</h2><div class="meta"><span>22.08.2014</span><span>Köln/ Altstadt</span></div></div><div class="actions"><div><svg width="11" height="9"><use href="#cart"/></svg></div><div><svg width="8" height="8"><use href="#zoom"/></svg></div></div></article>
  <article class="card"><div class="photo" style="height:163px" role="img" aria-label="Foto: kurzes Spitzenkleid"><span class="price">69,00 €</span><span class="cat">Brautmode</span></div><div class="info"><h2>Traumhaftes Hochzeitskleid in weiß</h2><div class="meta"><span>22.08.2014</span><span>Köln/ Altstadt</span></div></div><div class="actions"><div><svg width="11" height="9"><use href="#cart"/></svg></div><div><svg width="8" height="8"><use href="#zoom"/></svg></div></div></article>
  <article class="card"><div class="photo green" style="height:205px" role="img" aria-label="Foto: Braut im Ballkleid im Garten"><span class="price">69,00 €</span><span class="cat">Brautmode</span></div><div class="info"><h2>Traumhaftes Hochzeitskleid in weiß</h2><div class="meta"><span>22.08.2014</span><span>Köln/ Altstadt</span></div></div><div class="actions"><div><svg width="11" height="9"><use href="#cart"/></svg></div><div><svg width="8" height="8"><use href="#zoom"/></svg></div></div></article>
  <article class="card"><div class="photo green" style="height:205px" role="img" aria-label="Foto: Braut im Ballkleid im Garten"><span class="price">69,00 €</span><span class="cat">Brautmode</span></div><div class="info"><h2>Traumhaftes Hochzeitskleid in weiß</h2><div class="meta"><span>22.08.2014</span><span>Köln/ Altstadt</span></div></div><div class="actions"><div><svg width="11" height="9"><use href="#cart"/></svg></div><div><svg width="8" height="8"><use href="#zoom"/></svg></div></div></article>
</div>

<div class="col c3">
  <article class="card"><div class="photo green" style="height:205px" role="img" aria-label="Foto: Braut im Ballkleid im Garten"><span class="price">69,00 €</span><span class="cat">Brautmode</span></div><div class="info"><h2>Traumhaftes Hochzeitskleid in weiß</h2><div class="meta"><span>22.08.2014</span><span>Köln/ Altstadt</span></div></div><div class="actions"><div><svg width="11" height="9"><use href="#cart"/></svg></div><div><svg width="8" height="8"><use href="#zoom"/></svg></div></div></article>
  <article class="card"><div class="photo" style="height:141px;background:linear-gradient(180deg,#7b7f85,#d8d8d6 50%,#b9b9b7)" role="img" aria-label="Foto: drapiertes Brautkleid mit Blüte"><span class="price">69,00 €</span><span class="cat">Brautmode</span></div><div class="info"><h2>Traumhaftes Hochzeitskleid in weiß</h2><div class="meta"><span>22.08.2014</span><span>Köln/ Altstadt</span></div></div><div class="actions"><div><svg width="11" height="9"><use href="#cart"/></svg></div><div><svg width="8" height="8"><use href="#zoom"/></svg></div></div></article>
  <article class="card"><div class="photo" style="height:163px" role="img" aria-label="Foto: kurzes weißes Brautkleid"><span class="price">69,00 €</span><span class="cat">Brautmode</span></div><div class="info"><h2>Traumhaftes Hochzeitskleid in weiß</h2><div class="meta"><span>22.08.2014</span><span>Köln/ Altstadt</span></div></div><div class="actions"><div><svg width="11" height="9"><use href="#cart"/></svg></div><div><svg width="8" height="8"><use href="#zoom"/></svg></div></div></article>
  <article class="card"><div class="photo" style="height:163px" role="img" aria-label="Foto: kurzes weißes Brautkleid"><span class="price">69,00 €</span><span class="cat">Brautmode</span></div><div class="info"><h2>Traumhaftes Hochzeitskleid in weiß</h2><div class="meta"><span>22.08.2014</span><span>Köln/ Altstadt</span></div></div><div class="actions"><div><svg width="11" height="9"><use href="#cart"/></svg></div><div><svg width="8" height="8"><use href="#zoom"/></svg></div></div></article>
</div>

<div class="more">Mehr anzeigen</div>

<aside class="box" style="top:75px;height:200px">
  <h3>Kategorien</h3>
  <ul class="list">
    <li>Brautmode<i class="caret"></i></li><li>Schuhe<i class="caret"></i></li><li>Accessoires<i class="caret"></i></li><li>Formwäsche/ Dessous<i class="caret"></i></li><li>Bräutigam<i class="caret"></i></li><li>Empfang &amp; Geschenke<i class="caret"></i></li><li>Dekoration<i class="caret"></i></li><li class="foot">Alle Kategorien</li>
  </ul>
</aside>

<aside class="box promo">
  <h3>Anzeige aufgeben</h3>
  <p>Lorem ipsum dolor sit amet, con-setetur sadipscing elitr, sed diam nonumy eirmod tempor invidunt</p>
  <div class="reg">Neu Registrieren</div>
</aside>

<aside class="box banner">Hier kann<br>Ihr Werbebanner stehen</aside>

<aside class="box" style="top:498px;height:199px">
  <h3>Forum</h3>
  <ul class="list">
    <li>Schweißdrüsen absaugen...<span class="badge">20</span></li>
    <li>Lorem ipsuolor sit aet...<span class="badge">2</span></li>
    <li>Lom ipum dot amt<span class="badge">200</span></li>
    <li>Lorem ipsum domet<span class="badge">11</span></li>
    <li>Lorem ipsum dosit amet<span class="badge">11</span></li>
    <li>Lorem ipsu sit amet<span class="badge">20</span></li>
    <li>Lorem ipsum dolor sit amet...<span class="badge">11</span></li>
    <li class="foot">Hier geht es zum Forum</li>
  </ul>
</aside>

<aside class="box like">
  <h3>Schon gelikt?</h3>
  <div class="likehead"><div class="av" role="img" aria-label="Profilbild der Seite"></div><span class="likebtn">✓ Gefällt mir</span></div>
  <div class="likecount">Dir und 395 weiteren Personen gefällt</div>
  <div class="faces" role="img" aria-label="Profilbilder von neun Fans"></div>
  <div class="plug"><i></i>Soziales Plug-in von Plaudernetz</div>
</aside>

<aside class="box share">
  <h3>Seite empfehlen</h3>
  <p>Empfehlen und teilen Sie unsere Seite mit Ihren Freund-en und Bekannten</p>
  <div class="field">Empfehlen auf<i></i></div>
  <div class="field">Teilen auf<i></i></div>
  <div class="field">Empfehlen auf<i></i></div>
</aside>

<aside class="box news">
  <h3>Newsletter</h3>
  <div class="field">Emailadresse eingeben...<i style="display:flex;align-items:center;justify-content:center"><svg width="10" height="7" viewBox="0 0 10 7"><rect x=".5" y=".5" width="9" height="6" fill="none" stroke="#fff"/><path d="M.5 .5l4.5 3.5 4.5-3.5" fill="none" stroke="#fff"/></svg></i></div>
</aside>

<footer class="footer">
  <div>© 2014 hochzeitsbasar.de. Alle Rechte vorbehalten.</div>
  <div class="links">Über Uns &nbsp; Impressum &nbsp; Presse &nbsp; Jobs<br>Kontakt &nbsp; FAQ &nbsp; Datenschutzrichtlinie<br>Rechtliche Hinweise</div>
</footer>
</body>
</html>
```